business cards, stationary
lets see what you got
Use specific fonts
up to designer
Modern
Calvin Marsh
Director of Sales
1870 Quarrymill road, Suite 114 Burlington, On L4K 3P8
Calvin@sunlanejourneys.example
www.sunlanejourneys.example
BBM: 58720936
LOGO on back

```html
<!DOCTYPE html>
<html lang="en">
<head>
<meta charset="utf-8">
<title>Sun Lane Journeys — Stationery</title>
<link href="https://fonts.googleapis.com/css2?family=Nunito:wght@400;700;800&display=swap" rel="stylesheet">
<style>
  :root{
    --bg-center:#9a9a9a;
    --bg-edge:#6c6c6c;
    --paper:#ffffff;
    --purple:#5c2a6f;
    --purple-dark:#47205a;
    --green:#8cc63f;
    --ink:#4a4a4a;
    --ink-soft:#8a8a8a;
  }
  *{box-sizing:border-box;margin:0;padding:0}
  html,body{width:1200px;height:302px;overflow:hidden}
  body{
    font-family:"Nunito",sans-serif;
    background:radial-gradient(ellipse at 50% 45%,var(--bg-center),var(--bg-edge));
    position:relative;
  }
  .piece{position:absolute;background:var(--paper);box-shadow:0 2px 5px rgba(0,0,0,.35);overflow:hidden}
  .wave{position:absolute;left:0;bottom:0;width:100%;display:block}
  .brand{display:flex;align-items:center;gap:4px;font-weight:800;color:var(--green);white-space:nowrap;line-height:1}
  .brand .dot{border-radius:50%;background:var(--green);flex:none}

  /* hero mark */
  .hero-brand{position:absolute;left:29px;top:72px;font-size:15px}
  .hero-brand .dot{width:12px;height:12px}
  .hero-tagline{position:absolute;left:60px;top:93px;font-size:6px;color:#e0e0e0;letter-spacing:.3px}

  /* business cards */
  .card{width:151px;height:50px;left:29px}
  .card-front{top:130px}
  .card-back{top:194px}
  .card-front .who{position:absolute;left:7px;top:5px;font-size:5.5px;line-height:6px;color:var(--purple);font-weight:800}
  .card-front .role{position:absolute;left:7px;top:11px;font-size:3.6px;line-height:4px;color:var(--ink-soft)}
  .card-front .contact{position:absolute;left:7px;top:17px;font-size:3.2px;line-height:4px;color:var(--ink);width:80px}
  .card-front .brand{position:absolute;right:7px;top:6px;font-size:5.5px}
  .card-front .brand .dot{width:4px;height:4px}
  .card-back .brand{position:absolute;left:50%;top:15px;transform:translateX(-50%);font-size:8px}
  .card-back .brand .dot{width:6px;height:6px}

  /* letterheads */
  .letterhead{width:187px;height:245px;top:19px}
  .letterhead-a{left:293px}
  .letterhead-b{left:502px}
  .letterhead .brand{position:absolute;left:50%;top:11px;transform:translateX(-50%);font-size:7px}
  .letterhead .brand .dot{width:6px;height:6px}
  .letterhead .footer{position:absolute;left:0;right:0;bottom:5px;text-align:center;font-size:3.5px;color:#fff}

  /* compliment slips */
  .slip{width:199px;height:84px;left:708px}
  .slip-a{top:72px}
  .slip-b{top:178px}
  .slip .brand{position:absolute;left:10px;top:10px;font-size:7px}
  .slip .brand .dot{width:6px;height:6px}

  /* envelopes */
  .envelope{width:204px;left:948px}
  .envelope-a{top:58px;height:50px}
  .envelope-b{top:114px;height:66px}
  .envelope-c{top:186px;height:78px}
  .envelope .flap{position:absolute;left:0;top:0;width:100%;height:100%}
  .envelope-a .brand{position:absolute;left:10px;top:9px;font-size:7px;color:var(--paper)}
  .envelope-a .brand .dot{width:6px;height:6px}
</style>
</head>
<body>

  <div class="hero-brand brand"><span class="dot"></span>sunlanejourneys</div>
  <div class="hero-tagline">Holiday Travel</div>

  <div class="piece card card-front">
    <div class="who">Calvin Marsh</div>
    <div class="role">Director of Sales</div>
    <div class="contact">
      00 Sample Lane, Suite 000<br>Anytown<br>
      Calvin@sunlanejourneys.example<br>www.sunlanejourneys.example<br>BBM: 0000 0000
    </div>
    <div class="brand"><span class="dot"></span>sunlanejourneys</div>
    <svg class="wave" viewBox="0 0 151 9" preserveAspectRatio="none" height="9">
      <path d="M0 5 C45 0 95 8 151 1 L151 9 L0 9Z" fill="var(--green)"/>
      <path d="M0 7 C48 3 95 9 151 4 L151 9 L0 9Z" fill="var(--purple)"/>
    </svg>
  </div>

  <div class="piece card card-back">
    <div class="brand"><span class="dot"></span>sunlanejourneys</div>
    <svg class="wave" viewBox="0 0 151 14" preserveAspectRatio="none" height="14">
      <path d="M0 7 C45 1 95 12 151 2 L151 14 L0 14Z" fill="var(--green)"/>
      <path d="M0 10 C48 4 95 14 151 5 L151 14 L0 14Z" fill="var(--purple)"/>
    </svg>
  </div>

  <div class="piece letterhead letterhead-a">
    <div class="brand"><span class="dot"></span>sunlanejourneys</div>
    <svg class="wave" viewBox="0 0 187 32" preserveAspectRatio="none" height="32">
      <path d="M0 14 C60 2 125 24 187 6 L187 32 L0 32Z" fill="var(--green)"/>
      <path d="M0 18 C65 7 125 28 187 11 L187 32 L0 32Z" fill="var(--purple)"/>
    </svg>
    <div class="footer">www.sunlanejourneys.example</div>
  </div>

  <div class="piece letterhead letterhead-b">
    <div class="brand"><span class="dot"></span>sunlanejourneys</div>
    <svg class="wave" viewBox="0 0 187 32" preserveAspectRatio="none" height="32">
      <path d="M0 14 C60 2 125 24 187 6 L187 32 L0 32Z" fill="var(--green)"/>
      <path d="M0 18 C65 7 125 28 187 11 L187 32 L0 32Z" fill="var(--purple)"/>
    </svg>
    <div class="footer">www.sunlanejourneys.example</div>
  </div>

  <div class="piece slip slip-a">
    <div class="brand"><span class="dot"></span>sunlanejourneys</div>
    <svg class="wave" viewBox="0 0 199 20" preserveAspectRatio="none" height="20">
      <path d="M0 10 C65 2 130 18 199 4 L199 20 L0 20Z" fill="var(--green)"/>
      <path d="M0 13 C65 6 130 20 199 8 L199 20 L0 20Z" fill="var(--purple)"/>
    </svg>
  </div>

  <div class="piece slip slip-b">
    <div class="brand"><span class="dot"></span>sunlanejourneys</div>
    <svg class="wave" viewBox="0 0 199 24" preserveAspectRatio="none" height="24">
      <path d="M0 11 C65 2 130 20 199 4 L199 24 L0 24Z" fill="var(--green)"/>
      <path d="M0 15 C65 6 130 22 199 8 L199 24 L0 24Z" fill="var(--purple)"/>
    </svg>
  </div>

  <div class="piece envelope envelope-a" style="background:var(--purple)">
    <svg class="flap" viewBox="0 0 204 50" preserveAspectRatio="none">
      <path d="M0 0 L102 30 L204 0" fill="none" stroke="var(--purple-dark)" stroke-width="1"/>
      <path d="M0 41 C65 32 140 48 204 36 L204 50 L0 50Z" fill="var(--green)"/>
    </svg>
    <div class="brand"><span class="dot"></span>sunlanejourneys</div>
  </div>

  <div class="piece envelope envelope-b">
    <svg class="flap" viewBox="0 0 204 66" preserveAspectRatio="none">
      <path d="M0 0 L102 36 L204 0Z" fill="var(--purple)"/>
      <path d="M0 0 L102 30 L204 0" fill="none" stroke="var(--green)" stroke-width="2"/>
    </svg>
  </div>

  <div class="piece envelope envelope-c">
    <svg class="flap" viewBox="0 0 204 78" preserveAspectRatio="none">
      <path d="M0 0 L102 40 L204 0" fill="none" stroke="#d8d8d8" stroke-width="1"/>
      <path d="M0 78 L102 36 L204 78" fill="none" stroke="#e2e2e2" stroke-width="1"/>
    </svg>
  </div>

</body>
</html>
```